" Nosso público-alvo são empresas grandes e médias (nacionais e multi). Trabalhamos com times intactos (líder e seus subordinados diretos) ou times multi-funcionais (duas ou mais áreas que precisam trabalhar juntas). Nosso serviço consiste em apoiar times a desenvolver o teamwork (trabalho em equipe) de alta performance, necessário para que possam concretizar seus objetivos de negócio com sucesso. O trabalho se inicia com um workshop (que chamamos de Crew Forge) onde, através de práticas e ferramentas, ajudamos o time a reconhecer sua Forma de Operar Atual (pontos positivos e limitantes) e a desenhar sua Forma de Operar Futura (de mais alto potencial) necessária para entregar seus objetivos com sucesso. Em seguida, no mesmo workshop, o time desenha o plano de ação para desenvolver essa Forma de Operar Futura. Opcionalmente e se necessário, após o workshop apoiamos o time na implantação do Plano de Ação e o acompanhamos durante toda a jornada, com sessões de team coaching + ferramentas e práticas de desenvolvimento, até que a Forma de Operar Futura esteja implantada e gerando resultados. Nosso diferencial é integrar desenvolvimento de liderança em time (teamwork) com o negócio. "

```html
<!DOCTYPE html>
<html lang="pt-BR">
<head>
<meta charset="utf-8">
<title>Crew Forge – Cartão de visita</title>
<link rel="stylesheet" href="https://fonts.googleapis.com/css2?family=Open+Sans:wght@400;600;700&display=swap">
<style>
  :root {
    --page: #ececec;
    --card-dark: #4a4a4c;
    --card-dark-soft: #565658;
    --card-light: #ffffff;
    --accent: #e8833a;
    --ink: #3d3d3f;
    --ink-light: #ffffff;
  }
  * { box-sizing: border-box; margin: 0; padding: 0; }
  html, body {
    width: 1200px; height: 1200px; overflow: hidden;
    background: var(--page);
    font-family: "Open Sans", Arial, sans-serif;
  }
  .sheet {
    position: relative; width: 1200px; height: 1200px;
  }
  .card {
    position: absolute; left: 150px; width: 900px; height: 500px;
    border-radius: 28px;
    box-shadow: 0 10px 30px rgba(0,0,0,0.12);
    overflow: hidden;
  }
  .card--front { top: 80px; background: var(--card-dark); color: var(--ink-light); }
  .card--back { top: 620px; background: var(--card-light); }

  .front__pattern {
    position: absolute; left: -60px; top: 40px; width: 420px; height: 420px;
    border-radius: 50%;
    background: radial-gradient(circle, var(--card-dark-soft) 0%, var(--card-dark) 70%);
  }
  .front__name {
    position: absolute; right: 70px; top: 62px;
    font-size: 44px; color: var(--accent); font-weight: 400;
  }
  .front__name strong { font-weight: 700; }
  .contact {
    position: absolute; right: 70px; list-style: none;
    text-align: right; font-size: 25px; line-height: 1.6;
  }
  .contact--direct { top: 168px; }
  .contact--place { top: 350px; line-height: 1.45; }
  .contact li { display: flex; justify-content: flex-end; align-items: center; gap: 22px; }
  .contact strong { font-weight: 700; }
  .contact svg { width: 28px; height: 34px; flex: none; }

  .brand {
    position: absolute; inset: 0;
    display: flex; align-items: center; justify-content: center; gap: 22px;
  }
  .brand__dot { width: 34px; height: 34px; border-radius: 50%; background: var(--accent); }
  .brand__name { font-size: 92px; font-weight: 600; color: var(--ink); letter-spacing: 1px; }
</style>
</head>
<body>
<main class="sheet">
  <section class="card card--front" aria-label="Frente do cartão">
    <div class="front__pattern" role="img" aria-label="Padrão decorativo em relevo cinza"></div>
    <h1 class="front__name"><strong>Rafael</strong> Lenz</h1>
    <ul class="contact contact--direct">
      <li><span>+ 55 11 <strong>90000 1234</strong></span>
        <svg viewBox="0 0 28 34" aria-hidden="true"><rect x="6" y="2" width="16" height="30" rx="3" fill="none" stroke="var(--accent)" stroke-width="3"/><line x1="11" y1="27" x2="17" y2="27" stroke="var(--accent)" stroke-width="2.5"/></svg></li>
      <li><span>rafael@crewforge.com.br</span>
        <svg viewBox="0 0 28 34" aria-hidden="true"><text x="14" y="26" text-anchor="middle" font-family="Open Sans, sans-serif" font-size="28" font-weight="700" fill="var(--accent)">@</text></svg></li>
    </ul>
    <ul class="contact contact--place">
      <li>São Paulo/SP - Brasil</li>
      <li>www.crewforge.com.br</li>
    </ul>
  </section>

  <section class="card card--back" aria-label="Verso do cartão">
    <div class="brand">
      <span class="brand__dot" aria-hidden="true"></span>
      <span class="brand__name">Crew Forge</span>
    </div>
  </section>
</main>
</body>
</html>
```